Residential improvers, A Cozy Perch 2 Go *

Cozy Perch 2 Go is a real estate company specializing in turning unloved properties into improved, happy places to live. We specialize in thoughtfully-improved residential properties for buyers or renters. Our company needs a business card that reflects the renovated homes we create using green and Feng Shui principles,

Please disregard the images we submitted. We are looking for an abstract, sophisticated elegant design. No eggs in a nest ... nothing cute. The image can be soft.
Updates

Aloha (hello) all designers. We are a serious property investment/improvement company. We strive to be unique, renovating with style and elegance. Our business card must portray the same message. We thought the nest and flower might be "it" ... clearly it's not, once we saw what you submitted. Please revisit the brief as it was modified yesterday. Mahalo for your input! We look forward to hearing from all designers that have been invited.

Industry/Entity Type

Real Estate Development

Contact Information for Business Card

We will have separate business cards for
1) Corabeth Lindqvist 808-555-0173 corabeth@mailbrook.test
2) Marla Fenwright 808-555-0198 marlafenwright@mailbrook.test
** can we add the website later ... in the process of approval.
Investors * Renovators * Connectors

Font styles to use
Sans Serif

Colors
cadf82

Requirements
Must have
• a feng shui feel ... modern. Color - green with black print.
Nice to have
• A Cozy Perch 2 Go

```html
<!DOCTYPE html>
<html lang="en">
<head>
<meta charset="utf-8">
<title>Cozy Perch 2 Go — Business Card</title>
<link rel="stylesheet" href="https://fonts.googleapis.com/css2?family=Lato:wght@400&display=swap">
<style>
  :root {
    --stage: #141414;
    --card-top: #242526;
    --card-bottom: #1b1c1c;
    --ink-light: #ececec;
    --ink-soft: #d6d6d6;
    --leaf: #a9b965;
    --leaf-deep: #8e9e4e;
  }
  * { margin: 0; padding: 0; box-sizing: border-box; }
  html, body {
    width: 1200px; height: 443px; overflow: hidden;
    background: var(--stage);
    font-family: "Lato", sans-serif;
  }
  .stage { position: relative; width: 1200px; height: 443px; }
  .card {
    position: absolute; top: 90px; width: 478px; height: 274px;
    border-radius: 12px;
    background: linear-gradient(180deg, var(--card-top), var(--card-bottom));
    box-shadow: 3px 5px 6px rgba(0,0,0,0.55);
  }
  .card--front { left: 102px; }
  .card--back { left: 624px; }

  .wordmark {
    position: absolute; display: flex; align-items: center; gap: 8px;
    color: var(--ink-light); font-weight: 400; white-space: nowrap;
    transform: translateX(-50%);
  }
  .wordmark__square { width: 9px; height: 9px; background: var(--leaf); }
  .card--front .wordmark { left: 126px; top: 138px; font-size: 25px; }
  .card--back .wordmark { left: 240px; top: 124px; font-size: 36px; }
  .card--back .wordmark__square { width: 12px; height: 12px; }

  .divider {
    position: absolute; left: 242px; top: 74px; width: 1.5px; height: 114px;
    background: var(--leaf-deep);
  }
  .contact { position: absolute; left: 270px; top: 94px; color: var(--ink-soft); }
  .contact__name { font-size: 18px; color: var(--ink-light); margin-bottom: 16px; }
  .contact__line { display: flex; align-items: center; gap: 6px; font-size: 13px; height: 24px; }
  .contact__icon { width: 13px; height: 11px; flex: none; }

  .website {
    position: absolute; left: 0; right: 0; top: 236px; text-align: center;
    font-size: 13px; letter-spacing: 1.8px; color: var(--ink-soft);
  }
  .tagline {
    position: absolute; left: 0; right: 0; top: 219px; text-align: center;
    font-size: 14px; letter-spacing: 0.4px; color: var(--leaf);
  }
  .tagline__sep { margin: 0 10px; }
</style>
</head>
<body>
<main class="stage">
  <section class="card card--front" aria-label="Business card front">
    <div class="wordmark"><span class="wordmark__square"></span>Cozy Perch 2 Go</div>
    <div class="divider"></div>
    <div class="contact">
      <p class="contact__name">Corabeth Lindqvist</p>
      <p class="contact__line">
        <svg class="contact__icon" viewBox="0 0 13 11" aria-hidden="true">
          <path d="M1 3.5 Q6.5 0 12 3.5 L10.5 5 L8.5 3.8 L4.5 3.8 L2.5 5 Z" fill="var(--leaf)"/>
          <rect x="2.5" y="5.5" width="8" height="4.5" rx="1" fill="var(--leaf)"/>
        </svg>
        808-555-0173
      </p>
      <p class="contact__line">
        <svg class="contact__icon" viewBox="0 0 13 11" aria-hidden="true">
          <rect x="0.5" y="1.5" width="12" height="8" fill="var(--leaf)"/>
          <path d="M0.5 1.5 L6.5 6 L12.5 1.5" fill="none" stroke="#1f2021" stroke-width="1"/>
        </svg>
        corabeth@mailbrook.test
      </p>
    </div>
    <p class="website">www.cozyperch2go.test</p>
  </section>

  <section class="card card--back" aria-label="Business card back">
    <div class="wordmark"><span class="wordmark__square"></span>Cozy Perch 2 Go</div>
    <p class="tagline">Investors<span class="tagline__sep">I</span>Renovators<span class="tagline__sep">I</span>Connectors</p>
  </section>
</main>
</body>
</html>
```